Business Card for Hollin Ledger - A cannabis publication for executives.

I'd like some business cards for Hollin Ledger. The logo is done (great job!) and I need a card design I will use with PELT. I made it a short project to allow time for printing before an event. These will be standard sized cards (final artwork size 3.66" x 2.16" at 300dpi) with a final card size of 3.5" x 2.0". (See PELT.example if you need more info.) I might try rounded corners but am not sure yet. I think the design will work okay with rounded.

Hollin Ledger will be a bi-weekly publication for the cannabis industry. It is targeted to investors and industry executives, not consumers or pot smokers. So our market is more B2B. However I am open to creativity and making the card something people remark on.

My contact for card:

Dara Venholm
Founder/CEO
dara@hollinledger.example

2746 Marrow Lane
Boston MA 02391
(617)555-0193

Target Market(s)

Executives, Industry people and investors in the Cannabis sector.

Contact Information for Business Card

PELT does do double sided and the second side can be the same or different images. Only one side is required but use of the second side would be a bonus.

Font styles to use
Serif
Sans Serif
Decorative

Colors

Designer to choose colors to be used in the design.

Requirements
Must have
• Logo, contact info
Nice to have
• Style and design to make the card stand out in a crowd.

```html
<!DOCTYPE html>
<html lang="en">
<head>
<meta charset="utf-8">
<title>Hollin Ledger Business Card</title>
<link rel="stylesheet" href="https://fonts.googleapis.com/css2?family=Open+Sans:wght@400;600;700&display=swap">
<style>
  :root {
    --page: #e9e9e7;
    --paper: #ffffff;
    --ink: #222222;
    --brand-blue: #1473bd;
    --brand-green: #7cb233;
    --card-black: #1f1f1f;
    --reverse-ink: #ffffff;
  }
  * { margin: 0; padding: 0; box-sizing: border-box; }
  html, body {
    width: 1200px; height: 900px; overflow: hidden;
    background: var(--page);
    font-family: "Open Sans", Arial, sans-serif;
    color: var(--ink);
  }
  .sheet {
    position: relative; width: 1200px; height: 900px;
    display: flex; flex-direction: column; align-items: center; justify-content: center; gap: 40px;
  }
  .card {
    position: relative; width: 700px; height: 400px; overflow: hidden;
    box-shadow: 0 6px 18px rgba(0,0,0,0.18);
  }
  .card-back {
    background: var(--card-black);
    display: flex; align-items: center; justify-content: center;
  }
  .card-front { background: var(--paper); }
  .brand {
    display: flex; align-items: center; gap: 18px;
    font-family: "Open Sans", Arial, sans-serif; font-weight: 600;
    letter-spacing: -0.5px; white-space: nowrap;
  }
  .brand-mark { display: block; flex: none; }
  .card-back .brand { color: var(--reverse-ink); font-size: 54px; }
  .card-back .brand-mark { width: 46px; height: 46px; background: var(--reverse-ink); }
  .card-front .brand {
    position: absolute; left: 345px; top: 170px;
    color: var(--brand-blue); font-size: 46px;
  }
  .card-front .brand-mark { width: 40px; height: 40px; background: var(--brand-green); }
  .decor { position: absolute; inset: 0; }
  .holder { position: absolute; left: 92px; top: 26px; }
  .holder-name { font-size: 21px; font-weight: 700; line-height: 1.2; }
  .holder-name .first { color: var(--brand-blue); }
  .holder-name .last { color: var(--brand-green); }
  .holder-title { font-size: 15px; line-height: 1.3; }
  .address { position: absolute; left: 34px; top: 150px; font-size: 16px; line-height: 1.4; font-style: normal; }
  .contact { position: absolute; left: 34px; top: 222px; list-style: none; font-size: 16px; line-height: 1.6; }
  .contact li { display: flex; align-items: center; gap: 8px; }
  .contact svg { width: 13px; height: 13px; fill: var(--brand-green); flex: none; }
</style>
</head>
<body>
<main class="sheet">
  <section class="card card-back" aria-label="Card back">
    <div class="brand"><span class="brand-mark"></span>Hollin Ledger</div>
  </section>

  <section class="card card-front" aria-label="Card front">
    <svg class="decor" viewBox="0 0 700 400" width="700" height="400" aria-hidden="true">
      <polygon points="0,0 20,0 0,48" fill="var(--brand-green)"/>
      <polygon points="28,0 78,0 78,48 6,48" fill="var(--brand-blue)"/>
      <polygon points="0,318 300,318 290,338 0,338" fill="var(--brand-green)"/>
      <polygon points="312,338 700,338 700,400 284,400" fill="var(--brand-blue)"/>
    </svg>

    <div class="holder">
      <p class="holder-name"><span class="first">Dara</span> <span class="last">Venholm</span></p>
      <p class="holder-title">Founder/CEO</p>
    </div>

    <address class="address">2746 Marrow Lane<br>Boston MA 02391</address>

    <ul class="contact">
      <li><svg viewBox="0 0 24 24"><path d="M6.6 10.8a15.1 15.1 0 0 0 6.6 6.6l2.2-2.2c.3-.3.7-.4 1-.2 1.1.4 2.3.6 3.6.6.6 0 1 .4 1 1V20c0 .6-.4 1-1 1A17 17 0 0 1 3 4c0-.6.4-1 1-1h3.5c.6 0 1 .4 1 1 0 1.3.2 2.5.6 3.6.1.3 0 .7-.2 1z"/></svg>(617)555-0193</li>
      <li><svg viewBox="0 0 24 24"><path d="M2 5h20v14H2z M3.5 6.5 12 13l8.5-6.5" fill-rule="evenodd"/><path d="M2 5l10 8 10-8v1.8l-10 8-10-8z" fill="#fff"/></svg>dara@hollinledger.example</li>
    </ul>

    <div class="brand"><span class="brand-mark"></span>Hollin Ledger</div>
  </section>
</main>
</body>
</html>
```